you will use Ai to Copy the website Wanderbay.com to come up with the basic frame work and it will give you the understanding of how I would like Coachlend.com to be like. Coachlend.com is a peer to peer rv rental site very similar to both of the other rv rental sites the difference is that are commission based 20% and above per rental and we will be one flat monthly rate and they keep all the earnings. Below is photo that will help you with the color scheme and the look and feel of the design

1 page

```html
<!DOCTYPE html>
<html lang="en">
<head>
<meta charset="utf-8">
<title>Coachlend.com – Keep every dollar you earn</title>
<link href="https://fonts.googleapis.com/css2?family=Inter:wght@400;500;600;700;800&display=swap" rel="stylesheet">
<style>
  :root {
    --navy: #11243a;
    --text: #3f4a56;
    --muted: #8a949e;
    --faint: #b7bec5;
    --green: #43a047;
    --green-dark: #2e7d32;
    --green-soft: #e8f3e4;
    --red: #e5483b;
    --red-soft: #fde4e2;
    --line: #e6eaee;
    --grey-bg: #f6f8fa;
    --white: #ffffff;
  }
  * { box-sizing: border-box; margin: 0; padding: 0; }
  html, body { width: 1140px; height: 1200px; overflow: hidden; }
  body { font-family: "Inter", sans-serif; color: var(--navy); background: var(--white); position: relative; }

  .pricing { position: absolute; left: 0; top: 0; width: 1140px; height: 444px;
    background: linear-gradient(120deg, #eef6ea 0%, #f3f7f2 55%, #eef5ec 100%);
    border-bottom: 1px solid var(--line); }
  .pricing-copy { position: absolute; left: 146px; top: 12px; width: 400px; }
  .pricing h1 { font-size: 29px; line-height: 31px; font-weight: 800; letter-spacing: -0.8px; }
  .pricing .lead { margin-top: 9px; font-size: 12px; line-height: 19px; color: var(--text); }
  .steps { list-style: none; margin-top: 24px; }
  .step { display: flex; gap: 15px; margin-bottom: 14px; }
  .step-num { flex: none; width: 24px; height: 24px; border: 1.5px solid var(--green); border-radius: 50%;
    font-size: 8px; font-weight: 700; color: var(--green-dark); display: flex; align-items: center; justify-content: center; margin-top: 2px; }
  .step h3 { font-size: 11.5px; font-weight: 600; line-height: 14px; }
  .step p { margin-top: 5px; font-size: 10px; line-height: 15px; color: var(--text); }
  .btn-primary { position: absolute; left: 146px; top: 347px; width: 150px; height: 37px; border-radius: 19px;
    background: var(--green); color: var(--white); font-size: 11.5px; font-weight: 600;
    display: flex; align-items: center; justify-content: center; text-decoration: none; }

  .earn-card { position: absolute; left: 600px; top: 42px; width: 394px; height: 289px; background: var(--white);
    border-radius: 15px; overflow: hidden; box-shadow: 0 12px 30px rgba(17,36,58,0.10); }
  .earn-head { height: 51px; background: var(--navy); color: var(--white); font-size: 11px; font-weight: 600;
    padding-left: 21px; display: flex; align-items: center; }
  .earn-row { padding: 19px 21px 0; height: 95px; }
  .earn-row + .earn-row { border-top: 1px solid var(--line); height: 95px; }
  .earn-label { display: flex; align-items: center; gap: 8px; font-size: 10px; font-weight: 600; }
  .dot { width: 7px; height: 7px; border-radius: 50%; }
  .dot.red { background: var(--red); }
  .dot.green { background: var(--green); }
  .bar-line { display: flex; align-items: center; gap: 9px; margin-top: 10px; }
  .bar { height: 20px; border-radius: 10px; }
  .bar.other { width: 247px; background: var(--red-soft); border: 1.5px solid var(--red); }
  .bar.ours { width: 302px; background: var(--green-soft); border: 1.5px solid var(--green); }
  .amount { font-size: 12.5px; font-weight: 700; }
  .earn-note { margin-top: 7px; font-size: 9px; color: var(--muted); }
  .earn-foot { position: absolute; left: 0; bottom: 0; width: 100%; height: 49px; padding-left: 21px;
    background: linear-gradient(90deg, #eef6ea, #e3f1de); display: flex; align-items: center;
    font-size: 11px; color: var(--green-dark); }
  .earn-foot strong { font-size: 12.5px; font-weight: 700; margin: 0 3px; }

  .experiences { position: absolute; left: 0; top: 444px; width: 1140px; height: 507px; background: var(--grey-bg); }
  .section-title { font-size: 29px; font-weight: 800; letter-spacing: -0.8px; line-height: 34px; }
  .section-sub { font-size: 12px; line-height: 19px; color: var(--text); }
  .experiences .section-title { position: absolute; left: 146px; top: 60px; }
  .experiences .section-sub { position: absolute; left: 146px; top: 98px; width: 400px; }
  .trip-card { position: absolute; top: 166px; height: 281px; border-radius: 15px; overflow: hidden; color: var(--white); }
  .trip-photo { position: absolute; inset: 0; }
  .trip-shade { position: absolute; inset: 0; background: linear-gradient(180deg, rgba(10,20,30,0) 45%, rgba(12,22,34,0.88) 100%); }
  .trip-body { position: absolute; left: 21px; right: 6px; top: 164px; }
  .trip-body h3 { font-size: 18px; font-weight: 700; letter-spacing: -0.4px; line-height: 22px; }
  .trip-body p { margin-top: 12px; font-size: 9.5px; line-height: 14px; letter-spacing: -0.1px;
    white-space: nowrap; color: rgba(255,255,255,0.86); }
  .btn-ghost { position: absolute; left: 21px; top: 234px; width: 91px; height: 27px; border-radius: 14px;
    border: 1px solid rgba(255,255,255,0.55); background: rgba(255,255,255,0.14); color: var(--white);
    font-size: 10px; font-weight: 600; display: flex; align-items: center; justify-content: center; text-decoration: none; }

  .destinations { position: absolute; left: 146px; top: 951px; width: 848px; }
  .destinations .section-title { margin-top: 47px; }
  .destinations .section-sub { margin-top: 10px; }
  .city-grid { list-style: none; margin-top: 23px; display: grid; grid-template-columns: repeat(6, 127px);
    column-gap: 17.5px; align-items: start; }
  .city { display: flex; justify-content: space-between; align-items: flex-start; padding: 6px 0 7px;
    border-bottom: 1px solid var(--line); font-size: 10.5px; line-height: 15.5px; color: var(--text); }
  .city .count { font-size: 8px; color: var(--faint); padding-top: 1px; text-align: right; }
  .city .count.wrap { width: 26px; text-align: left; line-height: 14px; }
</style>
</head>
<body>

<section class="pricing">
  <div class="pricing-copy">
    <h1>Other platforms take 20%+.<br>We take nothing.</h1>
    <p class="lead">We believe RV owners deserve to keep every dollar they earn. That's why we replaced commission-based pricing with a simple, flat monthly subscription.</p>
    <ol class="steps">
      <li class="step"><span class="step-num">01</span><div><h3>List your RV for free</h3><p>Create a detailed listing with photos, pricing, and availability in minutes.</p></div></li>
      <li class="step"><span class="step-num">02</span><div><h3>Guests book directly</h3><p>Renters browse, message you, and book. You control who rents your RV.</p></div></li>
      <li class="step"><span class="step-num">03</span><div><h3>Get paid in full</h3><p>Unlike competitors who take 20%+ per booking, you keep 100% of your earnings every time.</p></div></li>
    </ol>
  </div>
  <a class="btn-primary" href="#">Start listing today</a>

  <div class="earn-card">
    <div class="earn-head">What you earn on a $3,000/mo rental</div>
    <div class="earn-row">
      <div class="earn-label"><span class="dot red"></span>Other platforms</div>
      <div class="bar-line"><div class="bar other"></div><span class="amount">$2,100</span></div>
      <div class="earn-note">After 30% commission</div>
    </div>
    <div class="earn-row">
      <div class="earn-label"><span class="dot green"></span>Coachlend.com</div>
      <div class="bar-line"><div class="bar ours"></div><span class="amount">$2,970</span></div>
      <div class="earn-note">After flat monthly fee only</div>
    </div>
    <div class="earn-foot">You keep <strong>$870 more</strong> per month 🎉</div>
  </div>
</section>

<section class="experiences">
  <h2 class="section-title">Experience the outdoors your way</h2>
  <p class="section-sub">From classic road trips to luxury glamping, every option comes from a real RV owner near you.</p>

  <article class="trip-card" style="left:146px;width:329px;">
    <div class="trip-photo" role="img" aria-label="Rolling green hills in Yosemite" style="background:linear-gradient(170deg,#6e9a4a 0%,#3f7a2c 45%,#2a5a25 70%,#1b3324 100%);"></div>
    <div class="trip-shade"></div>
    <div class="trip-body"><h3>Yosemite, CA</h3><p>Towering granite walls, ancient sequoias, and waterfalls. The<br>most iconic road trip destination in America.</p></div>
    <a class="btn-ghost" href="#">Find RVs here</a>
  </article>

  <article class="trip-card" style="left:490px;width:245px;">
    <div class="trip-photo" role="img" aria-label="Red rock canyon at dusk near Bayfield" style="background:linear-gradient(180deg,#5d6a80 0%,#b89aa0 30%,#8a5a5a 55%,#4a3a44 80%,#232a36 100%);"></div>
    <div class="trip-shade"></div>
    <div class="trip-body"><h3>Bayfield, CO</h3><p>Luxury glamping and riverside calm<br>between Durango &amp; Pagosa Springs.</p></div>
    <a class="btn-ghost" href="#">Find RVs here</a>
  </article>

  <article class="trip-card" style="left:750px;width:244px;">
    <div class="trip-photo" role="img" aria-label="Sunset over a lake in Texas Hill Country" style="background:linear-gradient(180deg,#4e5560 0%,#9a8b74 30%,#e8b454 48%,#8c6e44 62%,#3a3a34 80%,#1f2630 100%);"></div>
    <div class="trip-shade"></div>
    <div class="trip-body"><h3>Hill Country, TX</h3><p>Star-filled skies, spring-fed lakes, and<br>wildflower meadows as far as the eye can...</p></div>
    <a class="btn-ghost" href="#">Find RVs here</a>
  </article>
</section>

<section class="destinations">
  <h2 class="section-title">Popular RV rental destinations</h2>
  <p class="section-sub">Find owner-listed RVs in top cities across the US.</p>
  <ul class="city-grid">
    <li class="city"><span>Atlanta, GA</span><span class="count">316 RVs</span></li>
    <li class="city"><span>Austin, TX</span><span class="count">303 RVs</span></li>
    <li class="city"><span>Boston, MA</span><span class="count">427 RVs</span></li>
    <li class="city"><span>Chicago, IL</span><span class="count">417 RVs</span></li>
    <li class="city"><span>Columbus, OH</span><span class="count">432 RVs</span></li>
    <li class="city"><span>Dallas, TX</span><span class="count">338 RVs</span></li>
    <li class="city"><span>Houston, TX</span><span class="count">148 RVs</span></li>
    <li class="city"><span>Baton Rouge, LA</span><span class="count">164 RVs</span></li>
    <li class="city"><span>Oklahoma City, OK</span><span class="count">259 RVs</span></li>
    <li class="city"><span>Las Vegas, NV</span><span class="count">208 RVs</span></li>
    <li class="city"><span>Los Angeles, CA</span><span class="count">2,836 RVs</span></li>
    <li class="city"><span>Miami, FL</span><span class="count">165 RVs</span></li>
    <li class="city"><span>San Antonio, TX</span><span class="count">118 RVs</span></li>
    <li class="city"><span>San Diego, CA</span><span class="count">2,013 RVs</span></li>
    <li class="city"><span>San Francisco,<br>CA</span><span class="count wrap">1,044 RVs</span></li>
    <li class="city"><span>Seattle, WA</span><span class="count">946 RVs</span></li>
    <li class="city"><span>Phoenix, AZ</span><span class="count">521 RVs</span></li>
    <li class="city"><span>Portland, OR</span><span class="count">480 RVs</span></li>
  </ul>
</section>

</body>
</html>
```